Refrigeration & Air Conditioning modern and appealing

We want to design a business card that is modern and appealing using existing logo supplied

Front card
Residential Commercial Diary
RTA : AU071523
Licence L258907

Back card
Marcus Ovenly
Director
0491 352 406
info@frostvalecooling.com.au
www.frostvalecooling.com.au
• Air Conditioning
• Cool Rooms & Refrigeration
• Installation
• Service & Repair
• Preventative Maintenance

We offer 24/7 emergency service

```html
<!DOCTYPE html>
<html lang="en">
<head>
<meta charset="utf-8">
<title>Frostvale Business Card</title>
<link href="https://fonts.googleapis.com/css2?family=Poppins:wght@400;500;600;700&display=swap" rel="stylesheet">
<style>
  :root {
    --violet: #9d6bfb;
    --violet-line: #8f5ff0;
    --ink: #000000;
    --paper: #ffffff;
    --backdrop: #d6d6d6;
  }
  * { margin: 0; padding: 0; box-sizing: border-box; }
  html, body { width: 1200px; height: 2558px; overflow: hidden; }
  body {
    background: var(--backdrop);
    font-family: "Poppins", sans-serif;
    position: relative;
  }
  .card {
    position: absolute;
    left: 217px;
    width: 766px;
    height: 437px;
    background: var(--ink);
    border: 2px solid var(--violet);
    box-shadow: 0 6px 10px rgba(0,0,0,0.25);
    overflow: hidden;
  }
  .card--back { top: 820px; }
  .card--front { top: 1340px; }

  /* Back side */
  .brand-band {
    position: absolute; left: 0; top: 0; bottom: 0; width: 228px;
    background: var(--violet);
  }
  .brand-band__mark {
    position: absolute; left: 50%; top: 50%;
    transform: translate(-50%, -50%) rotate(-90deg);
    display: flex; align-items: center; gap: 14px;
    white-space: nowrap;
  }
  .brand-dot {
    width: 44px; height: 44px; border-radius: 50%;
    background: var(--paper);
  }
  .brand-name {
    font-weight: 700; font-size: 44px; letter-spacing: 1px;
    color: var(--paper);
  }
  .details { position: absolute; left: 272px; top: 68px; width: 460px; color: var(--paper); }
  .details__name { font-weight: 700; font-size: 37px; line-height: 1.1; color: var(--violet); }
  .details__role { font-weight: 500; font-size: 23px; line-height: 1.2; }
  .rule { height: 2px; width: 344px; background: var(--violet-line); }
  .details .rule:first-of-type { margin-top: 12px; }
  .contacts { list-style: none; margin: 14px 0 16px; }
  .contacts li {
    display: flex; align-items: center; gap: 8px;
    font-weight: 500; font-size: 16.5px; line-height: 28.5px;
  }
  .contacts svg { width: 16px; height: 16px; flex: none; }
  .services {
    list-style: none; margin-top: 10px;
    display: grid; grid-template-columns: 164px auto;
    font-weight: 500; font-size: 16px; line-height: 28px;
  }
  .services li::before { content: "•"; color: var(--violet); margin-right: 3px; }
  .services li.wide { grid-column: 1 / 3; }

  /* Front side */
  .front-mark {
    position: absolute; left: 0; right: 0; top: 150px;
    display: flex; justify-content: center; align-items: center; gap: 18px;
  }
  .front-mark .brand-dot { width: 80px; height: 80px; background: var(--violet); }
  .front-mark .brand-name { font-size: 52px; }
  .tagline-row {
    position: absolute; left: 0; right: 0; top: 342px;
    display: flex; align-items: center; gap: 24px;
  }
  .tagline-row .line { flex: 1; height: 2px; background: var(--violet-line); }
  .tagline {
    font-weight: 500; font-size: 17px; color: var(--violet); white-space: nowrap;
  }
  .registration {
    position: absolute; left: 0; right: 0; top: 380px; text-align: center;
    font-weight: 500; font-size: 16px; color: var(--paper);
  }
  .registration .sep { color: var(--violet); }
</style>
</head>
<body>

<section class="card card--back" aria-label="Business card, contact side">
  <div class="brand-band">
    <div class="brand-band__mark">
      <span class="brand-dot"></span>
      <span class="brand-name">FROSTVALE</span>
    </div>
  </div>
  <div class="details">
    <h1 class="details__name">Marcus Ovenly</h1>
    <p class="details__role">Director</p>
    <div class="rule"></div>
    <ul class="contacts">
      <li>
        <svg viewBox="0 0 24 24" fill="#9d6bfb"><path d="M6.6 10.8a15.1 15.1 0 0 0 6.6 6.6l2.2-2.2a1 1 0 0 1 1-.25 11.4 11.4 0 0 0 3.6.57 1 1 0 0 1 1 1V20a1 1 0 0 1-1 1A17 17 0 0 1 3 4a1 1 0 0 1 1-1h3.5a1 1 0 0 1 1 1c0 1.25.2 2.45.57 3.57a1 1 0 0 1-.25 1z"/></svg>
        0491 352 406
      </li>
      <li>
        <svg viewBox="0 0 24 24" fill="#9d6bfb"><path d="M3 5h18v14H3z"/><path d="M3 5l9 7 9-7" fill="none" stroke="#000" stroke-width="1.6"/></svg>
        info@frostvalecooling.com.au
      </li>
      <li>
        <svg viewBox="0 0 24 24" fill="none" stroke="#9d6bfb" stroke-width="2"><circle cx="12" cy="12" r="9"/><path d="M3 12h18M12 3c3 3 3 15 0 18M12 3c-3 3-3 15 0 18"/></svg>
        www.frostvalecooling.com.au
      </li>
    </ul>
    <div class="rule"></div>
    <ul class="services">
      <li>Air Conditioning</li>
      <li>Cool Rooms &amp; Refrigeration</li>
      <li>Installation</li>
      <li>Service &amp; Repair</li>
      <li class="wide">Preventative Maintenance</li>
    </ul>
  </div>
</section>

<section class="card card--front" aria-label="Business card, brand side">
  <div class="front-mark">
    <span class="brand-dot"></span>
    <span class="brand-name">FROSTVALE</span>
  </div>
  <div class="tagline-row">
    <span class="line"></span>
    <span class="tagline">Residential Commercial Diary</span>
    <span class="line"></span>
  </div>
  <p class="registration">RTA : AU071523 <span class="sep">|</span> Licence : L258907</p>
</section>

</body>
</html>
```